Virtual assistant company needs letterhead and email signature

We need a letterhead and email signature for our virtual assistant company - dayBramble (small w capital F). Our tag line is think ahead | dayBramble

The colours we would like used are;

#81788c
#dddbe1

For reference our business cards have used #81788c background colour and #dddbe1 text

The fonts we would like used are

Lora
Proxima Nova

Please check out our twitter and facebook for style and feel

Twitter: @daybramble
www.chatterlane.com/daybramble

Please also find attached our landing page and business cards for reference

Any questions please let us know

Thanks
E

Reason: We like the opportunity to receive furthur designs

```html
<!DOCTYPE html>
<html lang="en">
<head>
<meta charset="utf-8">
<title>dayBramble – Email Signature</title>
<link href="https://fonts.googleapis.com/css2?family=Lora:wght@400&family=Montserrat:wght@400&family=Noto+Sans:wght@400&display=swap" rel="stylesheet">
<style>
  :root {
    --brand-purple: #7b7289;
    --brand-purple-light: #8a8198;
    --brand-mist: #dddbe1;
    --page-bg: #ffffff;
    --page-frame: #e6e6e6;
    --caption-ink: #1a1a1a;
  }
  * { box-sizing: border-box; margin: 0; padding: 0; }
  html, body {
    width: 1200px;
    height: 900px;
    overflow: hidden;
    background: var(--page-bg);
  }
  .slide {
    position: relative;
    width: 1200px;
    height: 900px;
    border: 1px solid var(--page-frame);
  }
  .signature {
    position: absolute;
    left: 100px;
    top: 417px;
    width: 1000px;
    height: 66px;
    overflow: hidden;
  }
  .signature__texture {
    position: absolute;
    inset: 0;
    background: linear-gradient(90deg, var(--brand-purple) 0%, var(--brand-purple-light) 55%, var(--brand-purple) 100%);
  }
  .signature__content {
    position: relative;
    display: flex;
    align-items: center;
    height: 100%;
    padding-left: 24px;
    color: var(--brand-mist);
  }
  .brand {
    display: flex;
    flex-direction: column;
    align-items: flex-end;
  }
  .brand__name {
    font-family: "Lora", serif;
    font-size: 28px;
    line-height: 1;
    letter-spacing: 0.2px;
  }
  .brand__tagline {
    font-family: "Montserrat", sans-serif;
    font-size: 9px;
    margin-top: 4px;
    align-self: center;
  }
  .divider {
    width: 1px;
    height: 42px;
    background: var(--brand-mist);
    margin: 0 18px 0 18px;
  }
  .details {
    font-family: "Montserrat", sans-serif;
    font-size: 12px;
    line-height: 17px;
  }
  .details__contact span + span { margin-left: 10px; }
  .caption {
    position: absolute;
    left: 40px;
    top: 832px;
    font-family: "Noto Sans", sans-serif;
    font-size: 26px;
    color: var(--caption-ink);
  }
</style>
</head>
<body>
  <main class="slide">
    <section class="signature">
      <div class="signature__texture" role="img" aria-label="Faint hand-drawn sketch notes texture in muted purple"></div>
      <div class="signature__content">
        <div class="brand">
          <span class="brand__name">dayBramble</span>
          <span class="brand__tagline">think ahead | dayBramble</span>
        </div>
        <div class="divider"></div>
        <div class="details">
          <p class="details__line">Lorem ipsum dolor sit amet, consectetur adipiscing elit. Vivamus at eros tempor</p>
          <p class="details__contact"><span>Tel: 00000 000000</span><span>Fax: 000000 000000</span></p>
        </div>
      </div>
    </section>
    <p class="caption">Email Signature</p>
  </main>
</body>
</html>
```